Young Balance Wellness Network

We need a poster explaining that some children live with a disability called Vestibular Disorder. Feel free to ask question. We want you to respect our color code, same as our logo.

Here is our website : http://www.ybwnetwork.org/

We need to sensibilise people about this disability for children.

Industry/Entity Type

Charity

Font styles to use
Serif

Requirements
Must have
• 1. our logo (with all our details) + one of the photo of Maxim
• 2. design showing a child with a dizziness for exemple
• 3. a title saying : Aidez-nous à changer la vie des enfants vivant avec un problème vestibulaire
• 4.include the text attached (information flyer YBWN)
• Poster size : 24"X 36"
Should not have
• wheel chair

```html
<!DOCTYPE html>
<html lang="en">
<head>
<meta charset="utf-8">
<title>Young Balance Wellness Network – Poster</title>
<link href="https://fonts.googleapis.com/css2?family=Archivo+Black&family=Oswald:wght@600&family=Lato:wght@400;700&display=swap" rel="stylesheet">
<style>
  :root {
    --page-bg: #e6e6e6;
    --paper: #ffffff;
    --lime: #b8cc1c;
    --lime-light: #d6e22a;
    --sky: #2f9bd0;
    --sky-light: #4cc0ec;
    --navy-blue: #1b7aa8;
    --amber: #ea9a0a;
    --gold: #c9891a;
    --olive: #8aa01c;
    --orange-text: #f0a21e;
  }
  html, body {
    margin: 0;
    width: 1200px;
    height: 1200px;
    overflow: hidden;
    background: var(--page-bg);
  }
  .poster {
    position: absolute;
    left: 212px;
    top: 50px;
    width: 776px;
    height: 1100px;
    display: block;
  }
  .brand-name { font-family: "Lato", sans-serif; font-weight: 700; fill: var(--olive); }
  .title-young { font-family: "Archivo Black", sans-serif; fill: var(--navy-blue); }
  .title-balance { font-family: "Oswald", sans-serif; font-weight: 600; fill: var(--gold); }
  .title-wellness { font-family: "Lato", sans-serif; font-weight: 400; fill: var(--olive); }
  .title-network { font-family: "Lato", sans-serif; font-weight: 400; fill: var(--orange-text); }
  .web-address { font-family: "Lato", sans-serif; font-weight: 400; fill: #ffffff; letter-spacing: 5px; }
</style>
</head>
<body>
<svg class="poster" viewBox="0 0 852 1207" xmlns="http://www.w3.org/2000/svg">
  <defs>
    <linearGradient id="limeWash" x1="0" y1="0" x2="1" y2="1">
      <stop offset="0" stop-color="var(--lime)"/>
      <stop offset="0.6" stop-color="var(--lime-light)"/>
      <stop offset="1" stop-color="#a9bf14"/>
    </linearGradient>
    <linearGradient id="playgroundTones" x1="0" y1="0" x2="0" y2="1">
      <stop offset="0" stop-color="#ffffff"/>
      <stop offset="0.35" stop-color="#e9efe4"/>
      <stop offset="0.55" stop-color="#a6b98a"/>
      <stop offset="0.8" stop-color="#b7aea0"/>
      <stop offset="1" stop-color="#c9c3bb"/>
    </linearGradient>
    <linearGradient id="swooshBlue" x1="0" y1="1" x2="1" y2="0">
      <stop offset="0" stop-color="var(--sky)"/>
      <stop offset="0.5" stop-color="var(--sky-light)"/>
      <stop offset="1" stop-color="var(--sky)"/>
    </linearGradient>
    <linearGradient id="grassFade" x1="0" y1="0" x2="0" y2="1">
      <stop offset="0" stop-color="#ffffff"/>
      <stop offset="1" stop-color="#ebebeb"/>
    </linearGradient>
  </defs>

  <!-- paper -->
  <rect class="paper" width="852" height="1207" fill="var(--paper)"/>

  <!-- lower background wash -->
  <rect class="lower-wash" x="0" y="850" width="852" height="310" fill="url(#grassFade)"/>

  <!-- lime header area -->
  <path class="lime-field" d="M0 0 H852 V300 C810 520 660 690 440 710 L0 720 Z" fill="url(#limeWash)"/>

  <!-- blue swoosh -->
  <path class="blue-swoosh" d="M852 355 L852 395 C800 560 650 780 380 790 C260 793 160 765 95 722 C200 760 300 765 400 757 C620 735 760 560 800 305 Z" fill="url(#swooshBlue)"/>
  <path d="M800 305 C760 560 620 735 400 757" fill="none" stroke="#ffffff" stroke-width="5"/>

  <!-- rings -->
  <circle cx="300" cy="390" r="350" fill="#ffffff"/>
  <circle cx="300" cy="390" r="338" fill="none" stroke="var(--amber)" stroke-width="14"/>
  <circle cx="300" cy="390" r="322" fill="none" stroke="var(--sky)" stroke-width="7"/>

  <!-- photo area -->
  <circle class="photo-area" cx="300" cy="390" r="316" fill="url(#playgroundTones)" role="img" aria-label="Photo of a smiling young child with arms spread wide, spinning on a yellow playground roundabout"/>

  <!-- brand mark -->
  <circle cx="272" cy="170" r="40" fill="var(--sky-light)"/>
  <text class="brand-name" x="272" y="252" font-size="26" text-anchor="middle">YBWN</text>

  <!-- title -->
  <text class="title-young" x="426" y="912" font-size="98" text-anchor="middle">YOUNG</text>
  <text class="title-balance" x="95" y="1045" font-size="118" textLength="412" lengthAdjust="spacingAndGlyphs">BALANCE</text>
  <text class="title-wellness" x="522" y="996" font-size="48" textLength="245" lengthAdjust="spacingAndGlyphs">WELLNESS</text>
  <text class="title-network" x="524" y="1042" font-size="48" textLength="243" lengthAdjust="spacingAndGlyphs">network</text>

  <!-- footer -->
  <rect class="footer-band" x="0" y="1158" width="852" height="49" fill="var(--amber)"/>
  <path class="web-tab" d="M212 1140 H609 V1186 H212 Z" fill="var(--navy-blue)"/>
  <text class="web-address" x="410" y="1170" font-size="19" text-anchor="middle">www.ybwnetwork.org</text>
</svg>
</body>
</html>
```